Business Card Design

Melodrift Podcast

Industry/Entity Type

Business

Contact Information for Business Card

YOU ARE INVITED TO LISTEN
Stretch Your Mindset
Award Winning Melodrift Podcast
with Dr. Maren Holloway
www.drmarenholloway.example

555-781-3096

```html
<!DOCTYPE html>
<html lang="en">
<head>
<meta charset="utf-8">
<title>Melodrift Podcast – Business Card</title>
<link rel="stylesheet" href="https://fonts.googleapis.com/css2?family=Poppins:wght@600;700&family=Questrial&family=Great+Vibes&display=swap">
<style>
  :root {
    --wine-deep: #4a0307;
    --wine: #7a0a10;
    --crimson: #c3141c;
    --glow: #ff3a3a;
    --gold: #f8d96a;
    --white: #ffffff;
  }
  html, body {
    margin: 0;
    padding: 0;
    width: 1200px;
    height: 703px;
    overflow: hidden;
    background: var(--wine-deep);
  }
  .card {
    display: block;
    width: 1200px;
    height: 703px;
  }
  .headline {
    font-family: "Poppins", sans-serif;
    font-weight: 600;
    fill: var(--white);
  }
  .headline--strong {
    font-weight: 700;
  }
  .tagline {
    font-family: "Questrial", sans-serif;
    font-size: 30px;
    fill: var(--gold);
  }
  .host-name {
    font-family: "Great Vibes", cursive;
    font-size: 62px;
    fill: var(--white);
  }
  .contact {
    font-family: "Questrial", sans-serif;
    font-size: 32px;
    fill: var(--gold);
  }
  .backdrop-word {
    font-family: "Poppins", sans-serif;
    font-weight: 700;
    font-size: 200px;
    fill: var(--white);
    fill-opacity: 0.17;
  }
</style>
</head>
<body>
<svg class="card" viewBox="0 0 1200 703" xmlns="http://www.w3.org/2000/svg">
  <defs>
    <radialGradient id="card-bg" cx="0.45" cy="0.4" r="0.8">
      <stop offset="0" stop-color="#a0121a"/>
      <stop offset="0.55" stop-color="#6e070d"/>
      <stop offset="1" stop-color="#3d0206"/>
    </radialGradient>
    <radialGradient id="left-glow" cx="0.5" cy="0.5" r="0.5">
      <stop offset="0" stop-color="#e0242b" stop-opacity="0.55"/>
      <stop offset="1" stop-color="#e0242b" stop-opacity="0"/>
    </radialGradient>
    <radialGradient id="mic-tone" cx="0.45" cy="0.55" r="0.55">
      <stop offset="0" stop-color="#ffd9d6"/>
      <stop offset="0.18" stop-color="#ff3b3b"/>
      <stop offset="0.55" stop-color="#b3101a"/>
      <stop offset="1" stop-color="#5a0409" stop-opacity="0"/>
    </radialGradient>
  </defs>

  <rect class="background" width="1200" height="703" fill="url(#card-bg)"/>
  <ellipse class="background-glow" cx="300" cy="200" rx="320" ry="230" fill="url(#left-glow)"/>

  <g class="mic-photo" role="img" aria-label="Photograph of a vintage studio microphone glowing in red light with light streaks">
    <ellipse cx="860" cy="400" rx="330" ry="340" fill="url(#mic-tone)"/>
  </g>

  <text class="backdrop-word" x="590" y="450" text-anchor="middle"
        textLength="1115" lengthAdjust="spacingAndGlyphs"
        transform="rotate(-15.5 590 383)">PODCAST</text>

  <g class="invitation">
    <text class="headline" x="190" y="152" font-size="80" textLength="346" lengthAdjust="spacingAndGlyphs">YOU ARE</text>
    <text class="headline headline--strong" x="190" y="236" font-size="92" textLength="336" lengthAdjust="spacingAndGlyphs">INVITED</text>
    <text class="headline" x="190" y="314" font-size="78" textLength="351" lengthAdjust="spacingAndGlyphs">TO LISTEN</text>
  </g>

  <g class="details" text-anchor="middle">
    <text class="tagline" x="380" y="378">Stretch Your Mindset</text>
    <text class="tagline" x="380" y="417" textLength="540" lengthAdjust="spacingAndGlyphs">Award Winning Melodrift Podcast with</text>
    <text class="host-name" x="380" y="508">Dr. Maren Holloway</text>
    <text class="contact" x="380" y="582">555-781-3096</text>
    <text class="contact" x="380" y="625">www.drmarenholloway.example</text>
  </g>
</svg>
</body>
</html>
```